First and Only Single Serving Dental Tooth Powder Company NEEDS Packaging DESIGN

We need a packaging design for a new company based in Florida called 'BrisoTin'. We created the first and only single serving dental tooth powder, for use with or without water. This solves a world problem in numerous faucets. Our product is great for Travelers, Adventure Seekers, Military Personnel, Daily Commuters and any one else wanting the cleanest mouth and freshest breath.

- This is a front and back of a 4(four) by 6(six) package design needed

Target Market(s)

Travelers,Outdoorsman, Adventure seekers, Daily Commuters, and Military Personnel.

Industry/Entity Type

Dental

Requirements
Must have
• -This must fit a package with the dimensions of 4" x 6"
• -four inches by six inches.
• -Earthy/Naturalistic Appeal
• - This is a front and back of a 4(four) by 6(six) package design needed
• -The package will be a White Nylon/Mylar bag
Nice to have
• -Clean your teeth anywhere, anytime...
• -Simple, Convenient, Effective
• -BrisoTin activates without water
• -Proudly made in the USA.
• -Package contains 15 BrisoTin's.
• -The Flavor for the BrisoTin is "Tripple Berry"
• -BrisoTin is for the everyday person on-the-go.
• -Our Story..
• Brisotin was brought to life for moments when time is vital and packing light is a must. We were tired of the same old ordinary way of cleaning our teeth while outdoors, on our adventures, or traveling the globe. The old way required water for it's use which isn't always readily available. With BrisoTin, water is not necessary. The package you hold in your hand contains no ordinary product. In fact, the way you use it is extremely unique and simple.
• Directions: Rip, Pour, Swish, Dispense. Enjoy your adventure responsibly!
Should not have
• A bunch of clutter besides that I am open to ideas.

```html
<!DOCTYPE html>
<html lang="en">
<head>
<meta charset="utf-8">
<title>BrisoTin Packaging – Front and Back</title>
<link rel="stylesheet" href="https://fonts.googleapis.com/css2?family=Fira+Sans:ital,wght@0,400;0,500;1,700&family=Overpass:wght@500;600;700;800&display=swap">
<style>
  :root {
    --stage: #c6c6c6;
    --mint-top: #c6f9de;
    --mint-mid: #5fd393;
    --green-bottom: #1b8a47;
    --brand-green: #1e6a3b;
    --white: #ffffff;
    --flavor-blue: #1f5fc0;
    --tooth-white: #f2f4f3;
    --flag-red: #c8283a;
    --flag-blue: #2c3e82;
  }
  * { margin: 0; padding: 0; box-sizing: border-box; }
  html, body { width: 1200px; height: 1200px; overflow: hidden; }
  body { background: var(--stage); position: relative; font-family: "Overpass", sans-serif; }

  .panel {
    position: absolute;
    top: 168px;
    width: 545px;
    height: 817px;
    background: linear-gradient(180deg, var(--mint-top) 0%, var(--mint-mid) 40%, #2fb868 65%, var(--green-bottom) 100%);
  }
  .panel--front { left: 36px; }
  .panel--back { left: 619px; }

  .brand-name {
    position: absolute;
    left: 0; right: 0;
    text-align: center;
    font-family: "Overpass", sans-serif;
    font-weight: 800;
    color: var(--brand-green);
    letter-spacing: 1px;
  }
  .panel--front .brand-name { top: 195px; font-size: 84px; }
  .panel--back .brand-name { top: 205px; font-size: 50px; }

  .headline {
    position: absolute;
    font-family: "Fira Sans", sans-serif;
    color: var(--white);
    white-space: nowrap;
  }
  .headline--lead { left: 38px; top: 410px; font-size: 38px; font-weight: 400; }
  .headline--strong { left: 52px; top: 452px; font-size: 43px; font-weight: 700; font-style: italic; letter-spacing: 0.5px; }

  .tagline {
    position: absolute;
    left: 0; right: 0; top: 522px;
    text-align: center;
    font-family: "Fira Sans", sans-serif;
    font-weight: 500;
    font-size: 29px;
    line-height: 33px;
    color: var(--white);
  }

  .flavor {
    position: absolute;
    left: 170px; top: 660px;
    width: 204px; height: 33px;
    background: var(--white);
    border-radius: 5px;
    text-align: center;
    font-family: "Fira Sans", sans-serif;
    font-weight: 500;
    font-size: 24px;
    line-height: 34px;
    color: var(--flavor-blue);
    white-space: nowrap;
  }
  .count {
    position: absolute;
    left: 170px; top: 699px; width: 204px;
    text-align: center;
    font-weight: 600;
    font-size: 22px;
    color: var(--white);
  }

  .origin-badge {
    position: absolute;
    left: 26px; top: 680px;
    width: 156px; height: 96px;
    background: linear-gradient(160deg, var(--flag-blue) 0%, var(--flag-blue) 30%, var(--flag-red) 31%, #f1e9e9 60%, var(--flag-red) 100%);
    border-radius: 4px;
  }
  .origin-badge__text {
    position: absolute;
    left: 0; right: 0; top: 26px;
    text-align: center;
    font-weight: 700;
    font-size: 15px;
    line-height: 17px;
    color: #111;
  }

  .feature-badge {
    position: absolute;
    left: 396px; top: 628px;
    width: 112px; height: 158px;
    background: radial-gradient(ellipse at 40% 30%, var(--white) 0%, var(--tooth-white) 55%, #c9cecc 100%);
    border-radius: 40px 40px 30px 30px;
  }
  .feature-badge__text {
    position: absolute;
    left: 0; right: 0; top: 28px;
    text-align: center;
    font-weight: 800;
    font-size: 16px;
    line-height: 18px;
    color: var(--brand-green);
  }

  .story-title {
    position: absolute;
    left: 0; right: 0; top: 367px;
    text-align: center;
    font-weight: 700;
    font-size: 24px;
    letter-spacing: 1px;
    color: var(--white);
  }
  .story {
    position: absolute;
    left: 0; right: 0; top: 405px;
    text-align: center;
    font-weight: 600;
    font-size: 19.5px;
    line-height: 19.8px;
    color: var(--white);
    white-space: nowrap;
  }
  .story p + p { margin-top: 19.8px; }
</style>
</head>
<body>
  <section class="panel panel--front" aria-label="Package front">
    <div class="brand-name">BrisoTin</div>
    <div class="headline headline--lead">Brush your teeth</div>
    <div class="headline headline--strong">ANYWHERE, ANYTIME...</div>
    <div class="tagline">“BrisoTin is for the<br>everyday person on-the-go.”</div>
    <div class="origin-badge" role="img" aria-label="Waving American flag illustration">
      <div class="origin-badge__text">Proudly made<br>in the USA.</div>
    </div>
    <div class="flavor">"WILD BRAMBLE"</div>
    <div class="count">30 BrisoTins</div>
    <div class="feature-badge" role="img" aria-label="White tooth illustration">
      <div class="feature-badge__text">BrisoTin<br>ACTIVATES<br>Without<br>Water!</div>
    </div>
  </section>

  <section class="panel panel--back" aria-label="Package back">
    <div class="brand-name">BrisoTin</div>
    <h2 class="story-title">OUR STORY</h2>
    <div class="story">
      <p>Brisotin was brought to life for the moments<br>
      when time is vital and packing light is a must.<br>
      We were tired of the same old ordinary way<br>
      of brushing our teeth while outdoors,<br>
      on our adventures, or while traveling the globe.<br>
      The old way required water for its use which<br>
      isn't always readily available.<br>
      With BrisoTin, water is not necessary.<br>
      The package you hold in your hand<br>
      is no ordinary product.<br>
      In fact, the way you use it is extraordinarily simple<br>
      and its for extraordinary people<br>
      just like you!</p>
      <p>Rip, Pour, Swish, Dispense.<br>
      Enjoy your adventure responsibly!</p>
    </div>
  </section>
</body>
</html>
```